Web site for Life Coaching Consultant

I require a website for a life coaching business. I have a Tidal Netware account which I set up last week. I will need to be able to add articles and testimonials. The design should communicate that RL Harbor Lanterns is there to help people breakdown personal barriers and that we are an advocate to help them achieve personal goals.
Updates

Reason: I have some designers just accepting my invitation to submit so to give them a few days to submit. I have been thrilled with the quality of the submissions Thank you.

Hi everyone

I am loving all your designs.  The only feedback I can get from people is that they feel that the runner makes the web page look like a personal coach rather than a life coach that helps people with relations, career, and personal road blocks.

Sorry                                   

Reason: Hi I have increased the deadline as there has been so many amazing designs and some of you have asked to fine tune your entries. I would like to take this opportunity to thank you all. It is going to be a tough decision. I have put a few more pictures on the project page hoping this will help

Hi I just wanted to thank you all for your great designs.  As I got so many good designs I have asked people to vote.  I will be in touch in the next day or 2.

Cheers

Target Market(s)

People with self esteem issues either woman or girls, people who want to goal set and need an advocate

Industry/Entity Type

Life Coaching

Colors
d2a4cc
e567a6

Requirements
Must have
• must have bio section, logo, articles page, affirmation section and testimonial page.

```html
<!DOCTYPE html>
<html lang="en">
<head>
<meta charset="utf-8">
<title>RL Harbor Lanterns – Life Coaching</title>
<link href="https://fonts.googleapis.com/css2?family=Source+Sans+3:wght@400;600;700&display=swap" rel="stylesheet">
<style>
:root{
  --pink:#e8207a;
  --pink-dark:#b3195f;
  --pink-deep:#a61656;
  --page:#f7f7f7;
  --text:#555;
  --heading:#333;
  --sidebar-item:#efefef;
  --sky:#7fb2d6;
  --sea:#2c8cc0;
  --white:#fff;
}
*{box-sizing:border-box;margin:0;padding:0}
html,body{width:984px;height:1200px;overflow:hidden}
body{background:var(--page);font-family:"Source Sans 3",sans-serif;color:var(--text);position:relative}
.abs{position:absolute}

/* header */
.site-header{position:absolute;left:0;top:0;width:984px;height:70px;background:var(--page)}
.brand-mark{position:absolute;left:124px;top:6px;width:90px;height:90px;border-radius:50%;background:var(--white);border:6px solid var(--white);z-index:3}
.brand-mark::after{content:"";position:absolute;inset:4px;border-radius:50%;background:var(--pink)}
.brand-name{position:absolute;left:218px;top:28px;font-size:24px;font-weight:700;color:var(--pink);letter-spacing:.2px}
.search{position:absolute;left:622px;top:22px;width:235px;height:28px;border:1px solid var(--pink);border-radius:3px;background:var(--white);overflow:hidden}
.search span{position:absolute;left:12px;top:6px;font-size:11px;color:var(--pink)}
.search .search-btn{position:absolute;right:0;top:0;width:39px;height:100%;background:var(--pink)}

/* nav */
.main-nav{position:absolute;left:0;top:70px;width:984px;height:35px;background:var(--pink)}
.nav-phone{position:absolute;left:222px;top:9px;color:var(--white);font-size:13px;font-weight:600;display:flex;align-items:center;gap:8px}
.nav-links{position:absolute;left:381px;top:0;display:flex;height:35px}
.nav-links a{color:var(--white);text-decoration:none;font-size:11.5px;line-height:35px;padding:0 20px}
.nav-links a:first-child{background:var(--pink-dark);padding:0 21px}
.nav-links a:nth-child(2){padding-left:10px}

/* hero */
.hero{position:absolute;left:0;top:105px;width:984px;height:351px;overflow:hidden}
.hero-photo{position:absolute;inset:0;background:linear-gradient(180deg,var(--sky) 0%,#8dbedb 30%,var(--sea) 52%,#cfe2ee 75%,#e9eef2 100%)}
.hero-figure{position:absolute;left:470px;top:0;width:450px;height:351px;background:radial-gradient(ellipse at 60% 55%,#f4f2ef 0%,#e6ddd6 40%,rgba(230,221,214,0) 72%)}
.hero-title{position:absolute;left:189px;top:95px;color:var(--white);font-weight:700;font-size:43px;line-height:40px}
.hero-title span{display:block;padding-left:37px}
.hero-rule{position:absolute;left:160px;top:186px;width:236px;height:1px;background:var(--pink)}
.hero-text{position:absolute;left:189px;top:194px;width:300px;color:var(--white);font-size:11px;font-weight:600;line-height:17px}
.btn-solid{display:inline-block;background:var(--pink);color:var(--white);font-weight:700;border-radius:2px;text-align:center}
.hero-cta{position:absolute;left:352px;top:261px;width:93px;height:26px;line-height:26px;font-size:11px}
.arrow{position:absolute;top:151px;width:50px;height:50px;border-radius:50%}
.arrow-prev{left:69px;background:var(--pink)}
.arrow-next{left:865px;border:1.5px solid var(--pink)}
.arrow svg{position:absolute;left:17px;top:16px}
.dots{position:absolute;left:795px;top:324px;display:flex;gap:4px}
.dots i{width:14px;height:14px;border-radius:50%;border:1.5px solid var(--white)}
.dots i:first-child{background:var(--pink);border-color:var(--pink)}
.hero-band{position:absolute;left:0;top:456px;width:984px;height:6px;background:var(--pink-deep)}

/* service cards */
.service{position:absolute;top:499px;width:171px}
.service-photo{height:117px;border:1px solid #ccc;border-bottom:3px solid var(--pink);border-radius:2px}
.service h3{margin-top:10px;font-size:16px;font-weight:600;color:var(--pink);padding-bottom:3px;border-bottom:1px solid var(--pink)}
.service p{margin-top:6px;font-size:8.6px;line-height:15.6px;padding-left:1px}
.btn-outline{display:inline-block;width:70px;height:23px;line-height:21px;font-size:9px;text-align:center;border:1px solid var(--pink);color:var(--pink);background:var(--white);border-radius:2px;margin-top:13px}
.btn-small{width:70px;height:23px;line-height:23px;font-size:9px;margin-top:13px}
.divider{position:absolute;left:0;top:812px;width:984px;height:1px;background:#d8d8d8}

/* welcome */
.welcome-title{position:absolute;left:126px;top:838px;font-size:19px;font-weight:400;color:var(--heading)}
.welcome-title b{color:var(--pink);font-weight:700}
.welcome-photo{position:absolute;left:126px;top:884px;width:171px;height:156px;border:1px solid #ccc;border-radius:2px;background:linear-gradient(160deg,#e9edf0,#b7c3cb 55%,#6f7880)}
.welcome-copy{position:absolute;left:314px;top:882px;width:325px;font-size:9px;line-height:15.6px}
.welcome-copy p+p{margin-top:15.6px}
.welcome-btn{position:absolute;left:313px;top:1018px;width:70px;height:23px;line-height:23px;font-size:9px}

/* sidebar */
.sidebar{position:absolute;left:686px;top:838px;width:171px}
.sidebar h3{font-size:19px;font-weight:400;color:var(--heading);padding-bottom:6px;border-bottom:1px solid var(--pink)}
.sidebar ul{list-style:none;margin-top:5px}
.sidebar li{height:23px;margin-bottom:3.5px;background:var(--sidebar-item);font-size:10.5px;line-height:23px;padding-left:30px;color:#444;position:relative}
.sidebar li::before{content:"";position:absolute;left:14px;top:8px;width:5px;height:5px;border-right:1.5px solid #555;border-top:1.5px solid #555;transform:rotate(45deg)}
.sidebar li.active{background:var(--pink);color:var(--white)}
.sidebar li.active::before{border-color:var(--white)}

/* footer */
.site-footer{position:absolute;left:0;top:1111px;width:984px;height:65px;background:var(--pink)}
.footer-mark{position:absolute;left:132px;top:1092px;width:62px;height:62px;border-radius:50%;background:var(--white);border:5px solid var(--pink)}
.footer-name{position:absolute;left:112px;top:1145px;font-size:14px;font-weight:700;color:var(--white)}
.footer-contact{position:absolute;left:250px;top:1119px;color:var(--white);font-size:11px;line-height:17.5px}
.footer-contact dt{float:left;width:48px;clear:left}
.social{position:absolute;left:741px;top:1132px;display:flex;gap:8px}
.social i{width:23px;height:23px;border-radius:50%;background:var(--white)}
.copyright{position:absolute;left:0;top:1176px;width:984px;height:24px;background:var(--pink-deep);color:var(--white);font-size:9.5px;font-weight:600;line-height:24px;padding-left:125px}
</style>
</head>
<body>

<header class="site-header">
  <div class="brand-mark" aria-hidden="true"></div>
  <div class="brand-name">Harbor Lanterns</div>
  <div class="search">
    <span>Search here....</span>
    <div class="search-btn">
      <svg width="39" height="28" viewBox="0 0 39 28"><circle cx="18" cy="13" r="4.5" fill="none" stroke="#fff" stroke-width="2"/><line x1="21.3" y1="16.3" x2="24.5" y2="19.5" stroke="#fff" stroke-width="2.2" stroke-linecap="round"/></svg>
    </div>
  </div>
</header>

<nav class="main-nav">
  <div class="nav-phone">
    <svg width="9" height="15" viewBox="0 0 9 15"><rect x="1" y="1" width="7" height="13" rx="1.2" fill="none" stroke="#fff" stroke-width="1.4"/><line x1="3.5" y1="11.5" x2="5.5" y2="11.5" stroke="#fff" stroke-width="1.2"/></svg>
    0400 555 218
  </div>
  <div class="nav-links">
    <a href="#">Home</a><a href="#">Life Coaching</a><a href="#">Our Articles</a><a href="#">Testimonials</a><a href="#">About us</a><a href="#">Contact</a>
  </div>
</nav>

<section class="hero">
  <div class="hero-photo" role="img" aria-label="Photo of a joyful woman with arms raised on a sunny beach, blue sea behind her">
    <div class="hero-figure"></div>
  </div>
  <h1 class="hero-title">You can live<span>a better life</span></h1>
  <div class="hero-rule"></div>
  <p class="hero-text">Lorem ipsum dolor sit amet, consectetur adipisicing elit, sed do eiusmod tempor incididuntaliqua.</p>
  <a class="btn-solid hero-cta">START TODAY</a>
  <div class="arrow arrow-prev"><svg width="14" height="18" viewBox="0 0 14 18"><polyline points="10,2 3,9 10,16" fill="none" stroke="#fff" stroke-width="3"/></svg></div>
  <div class="arrow arrow-next"><svg width="14" height="18" viewBox="0 0 14 18"><polyline points="4,2 11,9 4,16" fill="none" stroke="#e8207a" stroke-width="3"/></svg></div>
  <div class="dots"><i></i><i></i><i></i><i></i></div>
</section>
<div class="hero-band"></div>

<article class="service" style="left:126px">
  <div class="service-photo" role="img" aria-label="Photo of colleagues in business attire working together at a laptop" style="background:linear-gradient(160deg,#dfe5ea,#8b97a3 55%,#2f3640)"></div>
  <h3>Work &amp; Career</h3>
  <p>Lorem ipsum dolor sit amet, consectetur adipisicing elit, sed do eiusmod tempor incididunt ut labore et dolore magna aliqua. Ut enim ad minim veniam, quis nostrud exercitation ullamco laboris nisi ut aliquip ex ea commodo consequat.</p>
  <a class="btn-solid btn-small">Read more</a>
</article>
<article class="service" style="left:313px">
  <div class="service-photo" role="img" aria-label="Photo of a smiling couple embracing in a bright kitchen" style="background:linear-gradient(160deg,#f3f3f1,#d9d5cf 50%,#9fb3c6)"></div>
  <h3>Love &amp; Relationships</h3>
  <p>Lorem ipsum dolor sit amet, consectetur adipisicing elit, sed do eiusmod tempor incididunt ut labore et dolore magna aliqua. Ut enim ad minim veniam, quis nostrud exercitation ullamco laboris nisi ut aliquip ex ea commodo consequat.</p>
  <a class="btn-outline">Read more</a>
</article>
<article class="service" style="left:500px">
  <div class="service-photo" role="img" aria-label="Photo of a happy family outdoors in autumn" style="background:linear-gradient(160deg,#c9b89a,#8a7a5a 45%,#6c8a3e 75%,#c0608c)"></div>
  <h3>Home &amp; Family</h3>
  <p>Lorem ipsum dolor sit amet, consectetur adipisicing elit, sed do eiusmod tempor incididunt ut labore et dolore magna aliqua. Ut enim ad minim veniam, quis nostrud exercitation ullamco laboris nisi ut aliquip ex ea commodo consequat.</p>
  <a class="btn-outline">Read more</a>
</article>
<article class="service" style="left:687px">
  <div class="service-photo" role="img" aria-label="Photo of a woman with arms raised on a beach" style="background:linear-gradient(180deg,#7fb2d6,#2c8cc0 55%,#dfe9ef)"></div>
  <h3>Life &amp; Living</h3>
  <p>Lorem ipsum dolor sit amet, consectetur adipisicing elit, sed do eiusmod tempor incididunt ut labore et dolore magna aliqua. Ut enim ad minim veniam, quis nostrud exercitation ullamco laboris nisi ut aliquip ex ea commodo consequat.</p>
  <a class="btn-outline">Read more</a>
</article>

<div class="divider"></div>

<h2 class="welcome-title">Welcome to our <b>RL Harbor Lanterns</b></h2>
<div class="welcome-photo" role="img" aria-label="Photo of three business people reviewing a document on a staircase"></div>
<div class="welcome-copy">
  <p>Lorem ipsum dolor sit amet, consectetur adipisicing elit, sed do eiusmod tempor incididunt ut labore et dolore magna aliqua. Ut enim ad minim veniam, quis nostrud exercitation ullamco laboris nisi ut aliquip ex ea commodo consequat. Duis aute irure dolor in reprehenderit in voluptate velit esse cillum dolore eu fugiat nulla pariatur.</p>
  <p>Duis aute irure dolor in reprehenderit in voluptate velit esse cillum dolore eu fugiat nulla pariatur.</p>
</div>
<a class="btn-solid welcome-btn">Read more</a>

<aside class="sidebar">
  <h3>Self Help Articles</h3>
  <ul>
    <li>Past Predicts Future?</li>
    <li class="active">The Time Of Your Life</li>
    <li>How to Find Love</li>
    <li>Self Test</li>
    <li>Your True Purpose</li>
    <li>Past Predicts Future?</li>
    <li>The Time Of Your Life</li>
  </ul>
</aside>

<footer class="site-footer"></footer>
<div class="footer-mark" aria-hidden="true"></div>
<div class="footer-name">Harbor Lanterns</div>
<dl class="footer-contact">
  <dt>Phone:</dt><dd>0400 555 218</dd>
  <dt>Email:</dt><dd>hello@harborlanterns.example</dd>
  <dt>Address:</dt><dd>PO Box 4120 Seacliff VIC 3190</dd>
</dl>
<div class="social" aria-label="Social links"><i></i><i></i><i></i><i></i></div>
<div class="copyright">Copyrights © 2014 &nbsp;|&nbsp; Harbor Lanterns</div>

</body>
</html>
```